Web Design Project

We need a design for the actual web.
http://mirela.vunto.example/
It will be a cakes and cupcakes online shop.

It is a one page site, with five anchors.

Inicio (Home)
Here it will show a brief explanation about our shop, just explaining we sell really nice cakes and cupcakes. Also we want to show a slide gallery, like the one it is working, but with not nice choosen pictures.

Productos/Tortas
This two anchors will be just one at the end, but I wanted to show the two options for accessing the different products, tabs or buttons. You can click on the firsts images on that links for see the "pop up image" with a better explanation of every product.

Contacto
Here it will show a little form, that will only appear in smartphones and maybe tablets, this form needs to be similar and much more simple than the principal form (the next anchor), so just focus on it once the next one its done.

Form
This will be the way the users will send the orders, its a complex form, focused on the UX. We dont want the user to type too much and we want it to surprise the user and fell really comfortable.

Industry/Entity Type

Tv

Requirements
Must have

• -Must have side menu, but you can redesign it completelly, but with the same structure
-Its important to focus all the content in the top and middle, we arent sure about users screens and it we set info at the footer, maybe its not gonna show (no scroll vertical).
-You can change all the colours of the site, we are open to new visions, you can surprise us.

```html
<!DOCTYPE html>
<html lang="es">
<head>
<meta charset="utf-8">
<title>Dulce Vela — Cupcakes y Tortas</title>
<link rel="stylesheet" href="https://fonts.googleapis.com/css2?family=Roboto+Condensed:wght@400;700&family=Arimo:wght@400&display=swap">
<style>
  :root {
    --bg-pink: #fde3f0;
    --bg-pink-edge: #fbc3de;
    --sidebar-top: #fbb0d6;
    --sidebar-bottom: #c0427f;
    --menu-item: #d0659c;
    --ribbon: #f1eef0;
    --ribbon-text: #5a3418;
    --brown: #211107;
    --brand-text: #7a2a55;
    --brand-dot: #e9559c;
    --cta-top: #f679b8;
    --cta-bottom: #e13c8c;
    --photo-main: #d9b67a;
    --photo-dark: #b58a52;
    --check: #9dbfb0;
    --arrow-bg: rgba(52, 48, 40, 0.85);
    --white: #ffffff;
    --social: #8aa2c6;
  }
  * { box-sizing: border-box; margin: 0; padding: 0; }
  html, body { width: 1200px; height: 748px; overflow: hidden; }
  body {
    position: relative;
    background: radial-gradient(ellipse at 50% 50%, #fff2f8 0%, var(--bg-pink) 45%, var(--bg-pink-edge) 100%);
    font-family: "Arimo", Arial, sans-serif;
  }
  .brand {
    position: absolute; left: 132px; top: 56px;
    display: flex; align-items: center; gap: 10px;
    font-family: "Roboto Condensed", sans-serif; font-weight: 700;
    font-size: 30px; line-height: 1; color: var(--brand-text);
    white-space: nowrap;
  }
  .brand-dot { width: 16px; height: 16px; border-radius: 50%; background: var(--brand-dot); }
  .social { position: absolute; left: 961px; top: 96px; display: flex; gap: 4px; list-style: none; }
  .social li { width: 21px; height: 21px; border-radius: 4px; background: var(--social); box-shadow: inset 0 -6px 8px rgba(0,0,0,0.15); }
  .sidebar {
    position: absolute; left: 116px; top: 145px; width: 167px; height: 526px;
    border-radius: 3px;
    background: linear-gradient(to bottom, var(--sidebar-top) 0%, #f39cc8 55%, var(--sidebar-bottom) 85%);
    box-shadow: 0 0 8px rgba(200, 80, 140, 0.25);
  }
  .sidebar-photo {
    position: absolute; left: 0; bottom: 0; width: 167px; height: 146px;
    border-radius: 0 0 3px 3px;
    background: linear-gradient(to bottom, rgba(192,66,127,0) 0%, #d683ac 55%, #b9607f 100%);
  }
  .ribbon { position: absolute; left: 81px; top: 147px; width: 234px; height: 40px; }
  .ribbon-label {
    position: absolute; left: 137px; top: 154px;
    font-family: "Roboto Condensed", sans-serif; font-size: 17px; color: var(--ribbon-text);
  }
  .menu { position: absolute; left: 121px; top: 208px; list-style: none; }
  .menu li {
    width: 157px; height: 21px; margin-bottom: 23px;
    background: var(--menu-item);
    border-bottom: 1px solid rgba(255,255,255,0.45);
    padding-left: 17px;
    font-family: "Roboto Condensed", sans-serif; font-size: 17px; line-height: 22px;
    color: var(--white);
  }
  .stage {
    position: absolute; left: 299px; top: 146px; width: 794px; height: 525px;
    background: var(--white);
  }
  .slide {
    position: absolute; left: 6px; top: 6px; width: 782px; height: 411px;
    background: radial-gradient(ellipse at 55% 40%, #f0d9a0 0%, var(--photo-main) 45%, var(--photo-dark) 100%);
  }
  .slide-arrow { position: absolute; top: 157px; width: 66px; height: 85px; background: var(--arrow-bg); }
  .slide-arrow.prev { left: 6px; }
  .slide-arrow.next { left: 721px; }
  .slide-arrow svg { display: block; }
  .trim { position: absolute; left: 0; top: 417px; width: 794px; height: 15px; background: var(--check); }
  .intro {
    position: absolute; left: 0; top: 432px; width: 794px; height: 93px;
    background: var(--brown);
    border-top: 1px dashed #6a4a30;
  }
  .intro::after {
    content: ""; position: absolute; left: 0; right: 0; bottom: 3px;
    border-bottom: 1px dashed #6a4a30;
  }
  .intro-text {
    position: absolute; left: 56px; top: 16px; width: 600px;
    font-size: 12.2px; line-height: 14.5px; color: var(--white);
  }
  .cta {
    position: absolute; left: 693px; top: 32px; width: 82px; height: 28px;
    border-radius: 12px;
    background: linear-gradient(to bottom, var(--cta-top), var(--cta-bottom));
    font-family: "Roboto Condensed", sans-serif; font-weight: 700; font-size: 14px;
    color: var(--white); text-align: center; line-height: 28px;
  }
</style>
</head>
<body>
  <div class="brand"><span class="brand-dot" aria-hidden="true"></span>Dulce Vela</div>

  <ul class="social" aria-label="Redes sociales">
    <li aria-label="Red social 1"></li>
    <li aria-label="Red social 2"></li>
    <li aria-label="Red social 3"></li>
    <li aria-label="Red social 4"></li>
    <li aria-label="Red social 5"></li>
  </ul>

  <nav class="sidebar">
    <div class="sidebar-photo" role="img" aria-label="Foto suave de un cupcake en tonos rosados"></div>
  </nav>
  <svg class="ribbon" viewBox="0 0 234 40" aria-hidden="true">
    <polygon points="0,10 30,6 30,40 12,40 22,24" fill="#e4dde1"/>
    <polygon points="234,10 204,6 204,40 222,40 212,24" fill="#e4dde1"/>
    <rect x="25" y="0" width="184" height="34" fill="var(--ribbon)"/>
    <polygon points="25,34 40,34 25,40" fill="#c9bfc5"/>
    <polygon points="209,34 194,34 209,40" fill="#c9bfc5"/>
  </svg>
  <div class="ribbon-label">WELCOME</div>
  <ul class="menu">
    <li>INICIO</li>
    <li>PRODUCTO</li>
    <li>TORTAS</li>
    <li>CONTACTO</li>
    <li>FORM</li>
  </ul>

  <main class="stage">
    <div class="slide" role="img" aria-label="Foto de cupcakes con crema amarilla y arándanos sobre una base de porcelana floral, con una etiqueta de la tienda"></div>
    <div class="slide-arrow prev" aria-label="Anterior">
      <svg width="66" height="85" viewBox="0 0 66 85"><polyline points="44,16 18,42 44,68" fill="none" stroke="#fff" stroke-width="2"/></svg>
    </div>
    <div class="slide-arrow next" aria-label="Siguiente">
      <svg width="66" height="85" viewBox="0 0 66 85"><polyline points="22,16 48,42 22,68" fill="none" stroke="#fff" stroke-width="2"/></svg>
    </div>
    <div class="trim"></div>
    <section class="intro">
      <p class="intro-text">Finalmente ya está disponible en Santiago de Chile nuestro catálogo de sabrosos Cupcakes y Tortas<br>Con ingredientes 100% naturales y elaborados artesanalmente<br>No solo hay que tener en cuenta la presentación fabulosa de los mismos, lo que más destacan nuestros clientes es el sabor exquisito y la textura</p>
      <div class="cta">CONTACTO</div>
    </section>
  </main>
</body>
</html>
```